Create a new dynamic Video Production company website

A new website for a video production company. It needs to be focused on the videos with an easy to use and versatile video player. I want to be able to update (add/remove/edit) the videos myself and change some other regular information like price lists. Current website is www.reelvanta.ca
The new pages will be - Home - Corporate - Ministry - Wedding - Events - Contact

I was asked about Wordpress - I am not against WordPress so long as the designing company sets everything up properly. I have had bad experiences with Wordpress security (and spam) so as long as those issues are addressed, I can work with Wordpress.

Requirements
Must have
• Video player that scales to different platforms - computers, tablets, cell phones etc.

```html
<!DOCTYPE html>
<html lang="en">
<head>
<meta charset="utf-8">
<title>Reelvanta Video Productions</title>
<link rel="stylesheet" href="https://fonts.googleapis.com/css2?family=Oswald:wght@400;500&family=Open+Sans:wght@400;600;700&family=Lato:wght@700&display=swap">
<style>
:root{
  --ink:#1f1f1f;
  --text:#444;
  --white:#fff;
  --grey-band:#e8e8e8;
  --row-alt:#e6e6e6;
  --row:#f4f4f4;
  --feature:#555;
  --footer:#2b2b2b;
  --line:#2a2a2a;
  --wood1:#6b5a4a;
  --wood2:#3e332b;
}
*{margin:0;padding:0;box-sizing:border-box}
html,body{width:1200px;height:3352px;overflow:hidden}
body{position:relative;background:var(--white);font-family:"Open Sans",Arial,sans-serif;color:var(--text)}
.abs{position:absolute}
h1,h2{font-family:"Oswald",Arial,sans-serif;font-weight:500;color:var(--ink);text-transform:uppercase}

/* header */
.site-header{left:0;top:0;width:1200px;height:103px;background:var(--white)}
.brand{left:98px;top:30px;display:flex;align-items:center;gap:10px;font-family:"Oswald",sans-serif;font-weight:500;font-size:30px;color:var(--ink);letter-spacing:1px}
.brand-dot{width:30px;height:30px;border-radius:50%;background:var(--ink)}
.main-nav{right:98px;top:38px;display:flex;gap:52px;font-family:"Open Sans",sans-serif;font-weight:600;font-size:15px;color:var(--ink)}

/* hero */
.hero{left:0;top:103px;width:1200px;height:505px;background:linear-gradient(135deg,var(--wood1),var(--wood2))}
.hero-title{right:98px;top:232px;font-family:"Oswald",sans-serif;font-size:52px;color:var(--white);letter-spacing:-0.5px;line-height:1}
.hero-text{right:98px;top:320px;width:520px;text-align:right;font-weight:600;font-size:17px;line-height:36px;color:var(--white)}
.hero-btn{left:970px;top:420px;width:132px;height:50px;border:2px solid var(--white);color:var(--white);font-size:15px;font-weight:600;display:flex;align-items:center;justify-content:center}
.hero-dots{left:1018px;top:506px;display:flex;gap:4px}
.hero-dots span{width:14px;height:14px;border-radius:50%;border:2px solid var(--white)}
.hero-dots span:first-child{background:var(--white)}
.hero-curve{left:0;top:520px}

/* about */
.section-title{font-size:30px;line-height:1}
.title-rule{height:2px;width:140px;background:var(--ink)}
.about-text{left:98px;top:800px;width:640px;font-size:13px;line-height:22px}
.dark-btn{background:var(--ink);color:var(--white);font-weight:600;font-size:13px;display:flex;align-items:center;justify-content:center}
.about-photo{left:755px;top:726px;width:347px;height:271px;border:2px solid #999;background:linear-gradient(135deg,#dfe3e0,#8b918d 60%,#3a3d3b)}

/* services */
.services{left:0;top:1080px;width:1200px;height:585px;background:var(--grey-band);border-top:4px solid var(--line);border-bottom:4px solid var(--line)}
.services-intro{left:150px;top:1196px;width:900px;text-align:center;font-size:13px;line-height:22px}
.service-card{width:231px}
.service-frame{width:231px;height:230px;background:var(--ink);padding:10px}
.service-photo{width:100%;height:100%}
.service-name{margin-top:28px;text-align:center;font-family:"Lato",sans-serif;font-weight:700;font-size:22px;color:var(--ink)}

/* packages */
.packages-sub{left:98px;top:1822px;font-weight:600;font-size:17px;color:var(--ink)}
.packages-text{left:98px;top:1858px;width:660px;font-size:13px;line-height:22px}
.package-list{list-style:none;font-size:14px}
.package-list li{height:33.5px;display:flex;align-items:center;gap:14px}
.package-list svg{flex:none}
.operator-photo{left:793px;top:1743px;width:407px;height:398px;background:linear-gradient(160deg,#f2f2f2,#bfbfbf 55%,#2a2a2a)}
.packages-bottom{left:0;top:2139px;width:1200px;height:3px;background:var(--line)}

/* pricing */
.price-card{background:var(--row);box-shadow:0 1px 3px rgba(0,0,0,.15);border-bottom:3px solid var(--ink)}
.price-head{background:var(--ink);color:var(--white);font-family:Arial,sans-serif;font-weight:700;font-size:20px;text-transform:uppercase;display:flex;align-items:flex-end;justify-content:center;padding-bottom:10px}
.price-card.featured .price-head{background:var(--feature);font-size:22px}
.price-badge{position:absolute;left:50%;transform:translateX(-50%);border-radius:50%;background:var(--ink);border:3px solid var(--white);color:var(--white);font-family:Arial,sans-serif;font-size:28px;display:flex;align-items:center;justify-content:center}
.featured .price-badge{background:var(--feature)}
.price-row{height:45px;display:flex;align-items:center;justify-content:center;font-family:Arial,sans-serif;font-size:13px;color:#333}
.price-row:nth-child(even){background:var(--row-alt)}
.price-btn{margin:20px auto 0;background:var(--ink);color:var(--white);font-family:Arial,sans-serif;font-size:13px;font-weight:700;display:flex;align-items:center;justify-content:center;border-radius:2px}
.featured .price-btn{background:var(--feature)}

/* footer */
.footer-bg{left:0;top:2830px}
.footer-title{left:98px;top:2926px;font-family:"Oswald",sans-serif;font-size:29px;color:var(--white)}
.contact-item{left:98px;display:flex;align-items:center;gap:20px;color:var(--white);font-weight:700;font-size:15px;line-height:25px}
.contact-icon{width:50px;height:50px;border-radius:50%;border:2px solid var(--white);display:flex;align-items:center;justify-content:center;flex:none}
.form-title{left:485px;top:2930px;color:var(--white);font-weight:600;font-size:19px}
.field{border:2px solid #ddd;color:#ddd;font-size:13px;padding:8px 8px}
.send-btn{left:485px;top:3194px;width:116px;height:40px;background:var(--white);color:var(--ink);font-weight:600;font-size:13px;display:flex;align-items:center;justify-content:center}
.footer-rule{left:98px;top:3268px;width:1004px;height:1px;background:#777}
.copyright{left:98px;top:3300px;color:var(--white);font-weight:600;font-size:13px}
.social{left:972px;top:3290px;display:flex;gap:5px}
.social span{width:40px;height:40px;border-radius:50%;border:2px solid var(--white)}
</style>
</head>
<body>

<header class="abs site-header">
  <div class="abs brand"><span class="brand-dot"></span>REELVANTA</div>
  <nav class="abs main-nav">
    <span>Home</span><span>Corporate</span><span>Ministry</span><span>Wedding</span><span>Events</span><span>Contact</span>
  </nav>
</header>

<section class="abs hero" role="img" aria-label="Film reels, clapperboard and camera on a dark wooden table"></section>
<h1 class="abs hero-title">Welcome to Reelvanta</h1>
<p class="abs hero-text">At Reelvanta Video Productions, we create unique and original video productions for Ministry.</p>
<div class="abs hero-btn">READ MORE</div>
<div class="abs hero-dots"><span></span><span></span><span></span><span></span><span></span></div>
<svg class="abs hero-curve" width="1200" height="90" viewBox="0 0 1200 90"><path d="M0 30 Q600 130 1200 30 V90 H0 Z" fill="#fff"/></svg>

<h2 class="abs section-title" style="left:98px;top:724px">About Reelvanta</h2>
<div class="abs title-rule" style="left:98px;top:768px"></div>
<p class="abs about-text">At Reelvanta Video Productions, we create unique and original video productions for Ministry, Corporate or Personal events that will teach, inspire, and relive special moments for years to come. Wedding and event videography, tribute videos, teaching and training video, promotional video productions, live events, and the list goes on. We examine every detail of our projects to ensure the highest quality product is provided for our customers. Allow us to bring your thoughts, ideas and dreams, into a custom video production.</p>
<div class="abs dark-btn" style="left:98px;top:965px;width:108px;height:40px">READ MORE</div>
<div class="abs about-photo" role="img" aria-label="Video camera on a tripod filming an event"></div>

<section class="abs services"></section>
<h2 class="abs section-title" style="left:0;width:1200px;text-align:center;top:1142px">Reelvanta Services</h2>
<p class="abs services-intro">Live Sermons, Teaching Videos, Promotional video, and Special Services are just a few of the places where video productions can enhance your ministry.</p>
<div class="abs service-card" style="left:98px;top:1301px"><div class="service-frame"><div class="service-photo" role="img" aria-label="Camera filming a church service" style="background:linear-gradient(135deg,#c9c3e8,#6b6a86)"></div></div><div class="service-name">MINISTRY</div></div>
<div class="abs service-card" style="left:355px;top:1301px"><div class="service-frame"><div class="service-photo" role="img" aria-label="Camera filming a wedding ceremony" style="background:linear-gradient(135deg,#dfeee0,#7a8c72)"></div></div><div class="service-name">WEDDINGS</div></div>
<div class="abs service-card" style="left:612px;top:1301px"><div class="service-frame"><div class="service-photo" role="img" aria-label="Cameras recording a corporate conference" style="background:linear-gradient(135deg,#f0c48a,#5a6f8a)"></div></div><div class="service-name">CORPORATE</div></div>
<div class="abs service-card" style="left:869px;top:1301px"><div class="service-frame"><div class="service-photo" role="img" aria-label="Camera operator at a live concert" style="background:linear-gradient(135deg,#f2d34a,#b0357e 60%,#3a1d3a)"></div></div><div class="service-name">EVENTS</div></div>

<h2 class="abs section-title" style="left:98px;top:1760px">Our Packages</h2>
<div class="abs title-rule" style="left:98px;top:1798px;width:110px"></div>
<p class="abs packages-sub">Funeral Homes click here for your business packages</p>
<p class="abs packages-text">Tribute videos are made from a compilation of photos or video and special words all set to music and thought fully designed to capture a specific feeling. All of our productions are professionally edited with transition and tasteful special effects.</p>
<ul class="abs package-list" style="left:98px;top:1948px">
  <li><svg width="14" height="14" viewBox="0 0 14 14"><circle cx="7" cy="7" r="6" fill="none" stroke="#1f1f1f" stroke-width="2"/><path d="M5.5 4 L8.5 7 L5.5 10" fill="none" stroke="#1f1f1f" stroke-width="2"/></svg>Weddings</li>
  <li><svg width="14" height="14" viewBox="0 0 14 14"><circle cx="7" cy="7" r="6" fill="none" stroke="#1f1f1f" stroke-width="2"/><path d="M5.5 4 L8.5 7 L5.5 10" fill="none" stroke="#1f1f1f" stroke-width="2"/></svg>Birthdays</li>
  <li><svg width="14" height="14" viewBox="0 0 14 14"><circle cx="7" cy="7" r="6" fill="none" stroke="#1f1f1f" stroke-width="2"/><path d="M5.5 4 L8.5 7 L5.5 10" fill="none" stroke="#1f1f1f" stroke-width="2"/></svg>Anniversaries</li>
  <li><svg width="14" height="14" viewBox="0 0 14 14"><circle cx="7" cy="7" r="6" fill="none" stroke="#1f1f1f" stroke-width="2"/><path d="M5.5 4 L8.5 7 L5.5 10" fill="none" stroke="#1f1f1f" stroke-width="2"/></svg>Special Occasions</li>
  <li><svg width="14" height="14" viewBox="0 0 14 14"><circle cx="7" cy="7" r="6" fill="none" stroke="#1f1f1f" stroke-width="2"/><path d="M5.5 4 L8.5 7 L5.5 10" fill="none" stroke="#1f1f1f" stroke-width="2"/></svg>Funerals</li>
</ul>
<ul class="abs package-list" style="left:400px;top:1948px">
  <li><svg width="14" height="14" viewBox="0 0 14 14"><circle cx="7" cy="7" r="6" fill="none" stroke="#1f1f1f" stroke-width="2"/><path d="M5.5 4 L8.5 7 L5.5 10" fill="none" stroke="#1f1f1f" stroke-width="2"/></svg>Promotions</li>
  <li><svg width="14" height="14" viewBox="0 0 14 14"><circle cx="7" cy="7" r="6" fill="none" stroke="#1f1f1f" stroke-width="2"/><path d="M5.5 4 L8.5 7 L5.5 10" fill="none" stroke="#1f1f1f" stroke-width="2"/></svg>Advertising</li>
  <li><svg width="14" height="14" viewBox="0 0 14 14"><circle cx="7" cy="7" r="6" fill="none" stroke="#1f1f1f" stroke-width="2"/><path d="M5.5 4 L8.5 7 L5.5 10" fill="none" stroke="#1f1f1f" stroke-width="2"/></svg>Trade Shows</li>
  <li><svg width="14" height="14" viewBox="0 0 14 14"><circle cx="7" cy="7" r="6" fill="none" stroke="#1f1f1f" stroke-width="2"/><path d="M5.5 4 L8.5 7 L5.5 10" fill="none" stroke="#1f1f1f" stroke-width="2"/></svg>Training Video</li>
</ul>
<div class="abs operator-photo" role="img" aria-label="Camera operator holding a professional video camera toward the viewer"></div>
<div class="abs packages-bottom"></div>

<h2 class="abs section-title" style="left:0;width:1200px;text-align:center;top:2206px">Our Pricing</h2>
<div class="abs title-rule" style="left:565px;top:2259px;width:70px"></div>

<div class="abs price-card" style="left:150px;top:2385px;width:243px;height:346px">
  <div class="price-head" style="height:87px">Monthly Plan</div>
  <div class="price-badge" style="top:-45px;width:90px;height:90px">$100</div>
  <div class="price-row">Nemo enim ipsam voluptatem</div>
  <div class="price-row">Quia voluptas sit aspernatur aut odit</div>
  <div class="price-row">Sed quia consequuntur magni</div>
  <div class="price-row">Eos qui ratione voluptatem sequi</div>
  <div class="price-btn" style="width:150px;height:40px">GET STARTED</div>
</div>
<div class="abs price-card featured" style="left:460px;top:2365px;width:278px;height:388px">
  <div class="price-head" style="height:98px">Forever Plan</div>
  <div class="price-badge" style="top:-48px;width:96px;height:96px">$250</div>
  <div class="price-row" style="height:47px;font-size:14px">Nemo enim ipsam voluptatem</div>
  <div class="price-row" style="height:47px;font-size:14px">Quia voluptas sit aspernatur aut odit</div>
  <div class="price-row" style="height:47px;font-size:14px">Sed quia consequuntur magni</div>
  <div class="price-row" style="height:47px;font-size:14px">Eos qui ratione voluptatem sequi</div>
  <div class="price-btn" style="width:170px;height:44px;margin-top:26px">GET STARTED</div>
</div>
<div class="abs price-card" style="left:807px;top:2385px;width:244px;height:346px">
  <div class="price-head" style="height:87px">Yearly Plan</div>
  <div class="price-badge" style="top:-45px;width:90px;height:90px">$300</div>
  <div class="price-row">Nemo enim ipsam voluptatem</div>
  <div class="price-row">Quia voluptas sit aspernatur aut odit</div>
  <div class="price-row">Sed quia consequuntur magni</div>
  <div class="price-row">Eos qui ratione voluptatem sequi</div>
  <div class="price-btn" style="width:150px;height:40px">GET STARTED</div>
</div>

<svg class="abs footer-bg" width="1200" height="522" viewBox="0 0 1200 522"><path d="M0 30 Q600 -10 1200 30 V522 H0 Z" fill="#2b2b2b"/></svg>
<div class="abs footer-title">Contact Us</div>
<div class="abs contact-item" style="top:3015px"><span class="contact-icon"><svg width="20" height="14" viewBox="0 0 20 14"><rect x="1" y="1" width="18" height="12" fill="none" stroke="#fff" stroke-width="2"/><path d="M1 1 L10 8 L19 1" fill="none" stroke="#fff" stroke-width="2"/></svg></span>contact@reelvanta.ca</div>
<div class="abs contact-item" style="top:3097px"><span class="contact-icon"><svg width="16" height="22" viewBox="0 0 16 22"><path d="M8 21 C3 14 1 11 1 8 A7 7 0 0 1 15 8 C15 11 13 14 8 21 Z" fill="none" stroke="#fff" stroke-width="2"/><circle cx="8" cy="8" r="2.5" fill="#fff"/></svg></span>Reelvanta,<br>Kestrel Falls ON Canada</div>
<div class="abs contact-item" style="top:3171px"><span class="contact-icon"><svg width="20" height="20" viewBox="0 0 20 20"><path d="M4 2 L8 2 L9 6 L7 8 C8 11 9 12 12 13 L14 11 L18 12 L18 16 C18 17 17 18 16 18 C8 18 2 12 2 4 C2 3 3 2 4 2 Z" fill="none" stroke="#fff" stroke-width="1.8"/></svg></span>519-555-0148</div>

<div class="abs form-title">Fill out the form below, and we'll contact you shortly.</div>
<div class="abs field" style="left:485px;top:2984px;width:290px;height:40px">First Name</div>
<div class="abs field" style="left:810px;top:2984px;width:290px;height:40px">Last Name</div>
<div class="abs field" style="left:485px;top:3037px;width:290px;height:41px">Phone Number</div>
<div class="abs field" style="left:810px;top:3037px;width:290px;height:41px">E-Mail Address</div>
<div class="abs field" style="left:485px;top:3093px;width:615px;height:83px">Message</div>
<div class="abs send-btn">SEND NOW</div>

<div class="abs footer-rule"></div>
<div class="abs copyright">Copyright © 2017 Reelvanta. All rights reserved</div>
<div class="abs social"><span></span><span></span><span></span></div>

</body>
</html>
```